nutrition ebook cover

i need a cover for a ebook designed, the book is called velvet ridge so i would like that somewhere on the cover. i would also like the word nutrition followed by my company logo that i have attached below somewhere on the cover( i have attached two logos and would like to see with both separatley), i would like this to be faded into the background if possible, perhaps in a upper or lower corner. i would also like to see options with and without the picture i have attached below. the look I'm going for is professional and clean. this is a fat loss, healthy eating booklet. the winning designer i would like to design the following pages within the book aswell no more than 10 pages, that i will provide all content for, i just need help with putting what i have on pdf in a way that looks professional and cool. this would ideally covered in the rate that is paid for the cover. i also have other booklets i need made so the winning designer will most likely get that work too at a later date for an additional fee of course.

Industry/Entity Type

Nutrition

Requirements
Nice to have
• Outside images are welcomed, happy to purchase any stock images used from a outside source

```html
<!DOCTYPE html>
<html lang="en">
<head>
<meta charset="utf-8">
<title>Velvet Ridge — Ebook Cover</title>
<link rel="stylesheet" href="https://fonts.googleapis.com/css2?family=Playfair+Display:wght@700&family=Josefin+Sans:wght@400&display=swap">
<style>
  :root {
    --slate-dark: #1f2a30;
    --slate-mid: #34434a;
    --wood-dark: #4a2a16;
    --wood-warm: #8a5632;
    --veg-green: #3f6e2a;
    --veg-orange: #c8642a;
    --seal-fill: rgba(245, 238, 230, 0.62);
    --seal-ring: rgba(255, 255, 255, 0.85);
    --ink: #262524;
    --mark: rgba(255, 255, 255, 0.72);
  }
  * { margin: 0; padding: 0; box-sizing: border-box; }
  html, body { width: 848px; height: 1200px; overflow: hidden; background: var(--slate-dark); }
  .cover { position: relative; width: 848px; height: 1200px; overflow: hidden; }
  .cover-photo {
    position: absolute; inset: 0;
    background:
      radial-gradient(ellipse 300px 460px at 270px 720px, var(--wood-warm) 0%, var(--wood-dark) 70%, transparent 100%),
      radial-gradient(circle 180px at 720px 560px, var(--veg-green) 0%, transparent 100%),
      radial-gradient(circle 120px at 740px 120px, var(--veg-orange) 0%, transparent 100%),
      linear-gradient(160deg, var(--slate-mid) 0%, var(--slate-dark) 100%);
  }
  .title-seal { position: absolute; left: 0; top: 0; width: 848px; height: 1200px; }
  .title {
    position: absolute; left: 26px; width: 480px; text-align: center; color: var(--ink);
  }
  .title-main {
    top: 560px;
    font-family: "Playfair Display", Georgia, serif;
    font-weight: 700; font-size: 112px; line-height: 1;
  }
  .title-sub {
    top: 718px;
    font-family: "Josefin Sans", Arial, sans-serif;
    font-weight: 400; font-size: 86px; line-height: 1; letter-spacing: 2px;
  }
  .brand-mark {
    position: absolute; right: 30px; bottom: 40px;
    display: flex; flex-direction: column; align-items: center; gap: 10px;
    font-family: "Josefin Sans", Arial, sans-serif; font-weight: 400;
    color: var(--mark); text-transform: uppercase; text-align: center;
  }
  .brand-dot { width: 22px; height: 22px; border-radius: 50%; background: var(--mark); }
  .brand-name { font-size: 34px; line-height: 1.05; letter-spacing: 3px; }
</style>
</head>
<body>
<main class="cover">
  <div class="cover-photo" role="img" aria-label="Overhead photo of a rustic wooden cutting board on a dark slate table surrounded by fresh vegetables: broccoli, carrot, cherry tomatoes, mushrooms, lemon, olive oil and a pepper mill"></div>

  <svg class="title-seal" viewBox="0 0 848 1200" aria-hidden="true">
    <circle cx="266" cy="696" r="240" fill="var(--seal-fill)"/>
    <circle cx="266" cy="696" r="247" fill="none" stroke="var(--seal-ring)" stroke-width="2"/>
  </svg>

  <h1>
    <span class="title title-main">Velvet</span>
    <span class="title title-sub">RIDGE</span>
  </h1>

  <div class="brand-mark">
    <span class="brand-dot"></span>
    <span class="brand-name">Harvest<br>Bench</span>
  </div>
</main>
</body>
</html>
```